pharmacy/travel clinic business card design

We need a business card for our new business called Brenwick Travel Clinic and Pharmacy. Our primary focus is doing consultations for people before travelling internationally and providing vaccinations and prescriptions for them. While the business is considered a pharmacy, it has more the look and feel of a doctor's office. The design should communicate a professional and trustworthy feel. I have attached a copy of the logo we are going to be using.
Updates
Thanks for the submissions.  If you haven`t been eliminated you are one of the finalists.  Decision will likely be made tomorrow.

Target Market(s)
Customers, other health care professionals, travel agents
Industry/Entity Type
Clinic
Look and feel
Each slider illustrates characteristics of the customer's brand and the style your logo design should communicate.

```html
<!DOCTYPE html>
<html lang="en">
<head>
<meta charset="utf-8">
<title>Brenwick Travel Clinic and Pharmacy – Business Card</title>
<link rel="stylesheet" href="https://fonts.googleapis.com/css2?family=Marcellus&family=Tinos:wght@400;700&display=swap">
<style>
  :root {
    --page-bg: #e9ebe6;
    --card-lime: #cdef7a;
    --card-white: #ffffff;
    --panel-blue: #7fcdef;
    --ink: #111111;
    --brand-blue: #1f6fb5;
    --brand-green: #8bc53f;
    --url-ink: #333333;
  }
  * { box-sizing: border-box; margin: 0; padding: 0; }
  html, body {
    width: 922px;
    height: 1200px;
    overflow: hidden;
    background: var(--page-bg);
  }
  .canvas {
    position: relative;
    width: 922px;
    height: 1200px;
  }
  .business-card {
    position: absolute;
    left: 51px;
    top: 350px;
    width: 820px;
    height: 500px;
    border-radius: 6px;
    background: linear-gradient(180deg, var(--card-lime) 0%, #e6f7b8 55%, var(--card-white) 100%);
    box-shadow: 0 6px 18px rgba(0,0,0,0.18);
    overflow: hidden;
  }
  .card-panels {
    position: absolute;
    inset: 0;
  }
  .holder-name {
    position: absolute;
    left: 130px;
    top: 108px;
    font-family: "Marcellus", serif;
    font-size: 30px;
    color: var(--ink);
  }
  .holder-title {
    position: absolute;
    left: 195px;
    top: 152px;
    font-family: "Marcellus", serif;
    font-size: 30px;
    color: var(--ink);
  }
  .brand-name {
    position: absolute;
    left: 440px;
    top: 70px;
    display: flex;
    align-items: center;
    gap: 14px;
  }
  .brand-dot {
    width: 34px;
    height: 34px;
    border-radius: 50%;
    background: var(--brand-blue);
    flex: none;
  }
  .brand-text {
    font-family: "Marcellus", serif;
    font-size: 34px;
    line-height: 1.08;
    color: var(--brand-blue);
  }
  .contact-list {
    position: absolute;
    left: 176px;
    top: 320px;
    list-style: none;
    font-family: "Tinos", serif;
    font-weight: 700;
    font-size: 24px;
    color: var(--ink);
  }
  .contact-item {
    display: flex;
    align-items: center;
    gap: 12px;
    height: 48px;
  }
  .contact-icon {
    width: 34px;
    height: 34px;
    flex: none;
  }
  .card-url {
    position: absolute;
    left: 0;
    right: 0;
    bottom: 10px;
    text-align: center;
    font-family: "Tinos", serif;
    font-weight: 700;
    font-size: 20px;
    color: var(--url-ink);
  }
</style>
</head>
<body>
<main class="canvas">
  <article class="business-card">
    <svg class="card-panels" width="820" height="500" viewBox="0 0 820 500" aria-hidden="true">
      <path class="panel-top" fill="var(--panel-blue)"
            d="M40,140 Q45,38 210,32 L780,30 L780,150 Q770,240 620,248 L48,262 Q40,262 40,254 Z"/>
      <path class="panel-bottom" fill="var(--panel-blue)"
            d="M48,284 L620,272 Q770,272 780,360 L780,452 L220,466 Q45,470 40,380 L40,292 Q40,284 48,284 Z"/>
    </svg>

    <div class="holder-name">Your Name Here</div>
    <div class="holder-title">Title</div>

    <div class="brand-name">
      <span class="brand-dot"></span>
      <span class="brand-text">Brenwick Travel Clinic<br>and Pharmacy</span>
    </div>

    <ul class="contact-list">
      <li class="contact-item">
        <svg class="contact-icon" viewBox="0 0 34 34" aria-hidden="true">
          <path d="M3,17 L17,5 L31,17 L27,17 L27,30 L20,30 L20,21 L14,21 L14,30 L7,30 L7,17 Z" fill="var(--ink)"/>
        </svg>
        <span>Your address here</span>
      </li>
      <li class="contact-item">
        <svg class="contact-icon" viewBox="0 0 34 34" aria-hidden="true">
          <rect x="1" y="4" width="32" height="26" rx="4" fill="var(--ink)"/>
          <rect x="6" y="10" width="22" height="15" fill="none" stroke="#fff" stroke-width="1.8"/>
          <path d="M6,10 L17,19 L28,10" fill="none" stroke="#fff" stroke-width="1.8"/>
        </svg>
        <span>hello@brenwickmail.com</span>
      </li>
      <li class="contact-item">
        <svg class="contact-icon" viewBox="0 0 34 34" aria-hidden="true">
          <circle cx="17" cy="17" r="15" fill="none" stroke="var(--ink)" stroke-width="2.4"/>
          <path d="M11,9 L14,9 L15.5,13 L13.5,14.5 Q15,19 19.5,20.5 L21,18.5 L25,20 L25,23 Q24,25 21,25 Q10,23 9,12 Q9,9 11,9 Z" fill="var(--ink)"/>
        </svg>
        <span>041598273</span>
      </li>
    </ul>

    <div class="card-url">www.brenwickclinic.com</div>
  </article>
</main>
</body>
</html>
```